Landscaping business card

We need a business card that reflects our business. We do lawncare and landscaping with all natural materials and have a great track record in the communities we serve: Newton, Brookline, Wellesley, Brighton, Watertown, and Waltham. We have been in business for 10 years.
Updates

I don't know the curvy fonts. Please keep the fonts fairly conservative.

Industry/Entity Type

Landscaping

Contact Information for Business Card

Harrow Landscaping
Dale Harrow
Founder and CEO
271 Fenwick Ave
Fenmoor, NH 03187

Requirements
Must have
• The color green

```html
<!DOCTYPE html>
<html lang="en">
<head>
<meta charset="utf-8">
<title>Harrow Landscaping – Business Card</title>
<link rel="stylesheet" href="https://fonts.googleapis.com/css2?family=Playfair+Display:wght@500&family=Nunito+Sans:wght@400;600&display=swap">
<style>
  :root {
    --paper-light: #fbfbfb;
    --paper-edge: #e4e4e4;
    --band-dark: #23631b;
    --band-mid: #2f8426;
    --band-bright: #3b9a2d;
    --band-deep: #1d5516;
    --seal-fill: #e6e4ee;
    --seal-ring: #cfccdb;
    --title-ink: #ffffff;
    --body-ink: #1b1b1b;
  }
  html, body {
    margin: 0;
    padding: 0;
    width: 1200px;
    height: 667px;
    overflow: hidden;
    background: var(--paper-edge);
  }
  .card {
    position: relative;
    width: 1200px;
    height: 667px;
    background: radial-gradient(ellipse at 50% 45%, var(--paper-light) 0%, #f1f1f1 55%, var(--paper-edge) 100%);
  }
  .card-art {
    position: absolute;
    inset: 0;
    display: block;
  }
  .brand-name {
    font-family: "Playfair Display", "Times New Roman", serif;
    font-weight: 500;
    font-size: 70px;
    fill: var(--title-ink);
    letter-spacing: 0.8px;
  }
  .person-name {
    font-family: "Nunito Sans", Arial, sans-serif;
    font-weight: 400;
    font-size: 57px;
    fill: var(--body-ink);
  }
  .person-title {
    font-family: "Nunito Sans", Arial, sans-serif;
    font-weight: 400;
    font-size: 23px;
    fill: var(--body-ink);
    letter-spacing: 0.3px;
  }
  .address {
    font-family: "Nunito Sans", Arial, sans-serif;
    font-weight: 400;
    font-size: 38px;
    fill: var(--body-ink);
  }
</style>
</head>
<body>
  <main class="card">
    <svg class="card-art" width="1200" height="667" viewBox="0 0 1200 667" aria-labelledby="card-title">
      <title id="card-title">Harrow Landscaping business card for Dale Harrow</title>
      <defs>
        <linearGradient id="band-gradient" x1="0" y1="0" x2="1" y2="0">
          <stop offset="0" stop-color="var(--band-mid)"/>
          <stop offset="0.3" stop-color="var(--band-dark)"/>
          <stop offset="0.6" stop-color="var(--band-bright)"/>
          <stop offset="1" stop-color="var(--band-deep)"/>
        </linearGradient>
        <filter id="soft-shadow" x="-20%" y="-20%" width="140%" height="140%">
          <feDropShadow dx="4" dy="6" stdDeviation="6" flood-color="#000" flood-opacity="0.25"/>
        </filter>
      </defs>

      <rect class="brand-band" x="0" y="159" width="1200" height="157" fill="url(#band-gradient)"/>

      <circle class="brand-dot" cx="251" cy="239" r="150" fill="var(--seal-fill)" stroke="var(--seal-ring)" stroke-width="6" filter="url(#soft-shadow)"/>

      <text class="brand-name" x="465" y="233">HARROW</text>
      <text class="brand-name" x="465" y="297">LANDSCAPING</text>

      <text class="person-name" x="465" y="417">Dale Harrow</text>
      <text class="person-title" x="507" y="466">FOUNDER and CEO</text>

      <text class="address" x="466" y="543">271 Fenwick Ave</text>
      <text class="address" x="466" y="589">Fenmoor, NH 03187</text>
    </svg>
  </main>
</body>
</html>
```